Webshop for baby shoes need new design

We are an innovative company selling a one of a kind product on a market with tough competition. We are looking to step up our business and need a new design for our shop.

We are looking for recognition as well as originality. The customer must immediately be able to identify navigation, shopping cart, buy buttons etc. We want warm welcoming colors, but not too strong as to not draw attention away from the products. Retro might be interesting, if "done right".

Suggested color palette: http://huepalettemaker.example/#7k29WbQx3p8r5

We have a logo (attached), but if you have a better idea we might go for that instead. Also, a couple of product images are attached for you to use in the design.

What we do NOT want is a shop that looks like a free template (vendaForge etc). Also, while we are selling baby shoes, we don't want to use the very worn our baby pink/blue scheme, so stay clear of this, thanks.
Updates

We suggest that you use this palette, or similar: http://huepalettemaker.example/#7k29WbQx3p8r5

Project Deadline Extended
Reason: We feel that we are getting closer to finding a design that we like, but there is still a bit to go. Also we want to give the chance to any late starters to show their idea. The competition is still open.

Target Market(s)

babies and their parents

Industry/Entity Type

Shopping

Requirements
Must have
• The usual webshop elements
- shopping cart
- product listing
- product page
- buy buttons
Nice to have
• - large footer area for links, info and function (see trindel.example for an example)
- some kind of product navigation/filter (left, top or right)
- place for promotion banners

```html
<!DOCTYPE html>
<html lang="en">
<head>
<meta charset="utf-8">
<title>Tovlark – Baby Shoes</title>
<link rel="stylesheet" href="https://fonts.googleapis.com/css2?family=Roboto+Condensed:wght@400;700&family=Open+Sans:wght@400;600;700&family=Ubuntu:wght@400;500;700&family=Pacifico&display=swap">
<style>
:root{
  --paper:#efe6d4;
  --paper-dark:#e4d6bb;
  --band:#e6d5b5;
  --panel:#ede3cf;
  --brown:#8b5a2b;
  --brown-dark:#6b4423;
  --ink:#4a3a2a;
  --orange:#e08a1e;
  --footer:#8c7350;
  --footer-dark:#7a6243;
  --white:#ffffff;
  --card-border:#e0c9a1;
}
*{box-sizing:border-box;margin:0;padding:0}
html,body{width:896px;height:1200px;overflow:hidden;background:var(--paper)}
body{font-family:"Open Sans",sans-serif;color:var(--ink)}
.page{position:relative;width:896px;height:1200px;overflow:hidden;background:var(--paper)}
a{color:inherit;text-decoration:none}

/* header */
.header{position:absolute;left:0;top:0;width:896px;height:119px;background:var(--paper)}
.account{position:absolute;left:46px;top:7px;font-size:10px;color:var(--brown)}
.account span{color:#b59a78;margin:0 4px}
.cart{position:absolute;right:45px;top:6px;text-align:right;font-size:10px;color:var(--ink)}
.cart b{font-weight:700}
.cart-buttons{margin-top:6px;display:flex;gap:3px;justify-content:flex-end}
.cart-buttons a{background:var(--brown);color:var(--white);font-size:8px;padding:2px 6px;border-radius:2px}
.cart-buttons a.dark{background:#5e5446}
.nav-band{position:absolute;left:0;top:73px;width:896px;height:46px;background:linear-gradient(var(--band),#dcc7a2);border-top:1px solid #d4bd94;border-bottom:1px solid #cfb68b}
.nav{position:absolute;top:73px;height:46px;display:flex;align-items:center;font-family:"Roboto Condensed",sans-serif;font-size:13px;color:var(--brown-dark)}
.nav.left{left:76px}
.nav.right{left:572px}
.nav a{padding:0 22px;border-right:1px solid #cdb48a}
.nav a:last-child{border-right:none}
.nav a.active{background:#c89a48;border-radius:8px;padding:4px 12px;margin-right:22px;color:#3c2610;font-weight:700;border-right:none}
.brand-block{position:absolute;left:344px;top:0;width:210px;height:119px;background:linear-gradient(#e9dcc0,#dcc8a2);box-shadow:0 0 4px rgba(0,0,0,.15)}
.brand{position:absolute;left:0;right:0;top:62px;text-align:center;font-family:"Ubuntu",sans-serif;font-weight:700;font-size:31px;color:var(--brown)}
.brand-mark{position:absolute;left:86px;top:14px;width:38px;height:38px;background:var(--brown);border-radius:6px}

/* hero */
.hero{position:absolute;left:0;top:119px;width:896px;height:342px;background:var(--paper)}
.hero-title{position:absolute;left:68px;top:54px;font-family:"Pacifico",cursive;font-weight:400;font-size:31px;line-height:44px;color:var(--orange);white-space:nowrap}
.hero-text{position:absolute;left:68px;top:125px;width:340px;font-size:9.2px;line-height:15px;color:var(--ink)}
.btn{display:inline-block;background:var(--brown);color:var(--white);font-weight:700;border-radius:3px}
.hero-btn{position:absolute;left:160px;top:198px;font-size:10px;padding:5px 9px}
.hero-kid{position:absolute;left:258px;top:165px;width:135px;height:165px;border-radius:40% 40% 20% 20%;background:radial-gradient(circle at 50% 40%,#b9a68a,#d9ccb6 70%,transparent 72%)}
.hero-shoe{position:absolute;left:407px;top:43px;width:423px;height:250px;border-radius:45% 55% 20% 20%;background:linear-gradient(160deg,#2e6f84,#1f5566 60%,#e9e4d6 80%)}
.arrow{position:absolute;top:205px}
.arrow.prev{left:32px}
.arrow.next{right:32px}
.dots{position:absolute;left:412px;top:319px;display:flex;gap:8px}
.dots i{width:8px;height:8px;border-radius:50%;background:#d2b98f}
.dots i.on{background:var(--brown-dark)}

/* product cards */
.cards{position:absolute;left:0;top:461px;width:896px;height:240px;background:var(--white)}
.card{position:absolute;top:16px;width:187px;height:205px;background:var(--panel);border:1px solid var(--card-border);border-radius:3px;text-align:center}
.card h3{height:29px;line-height:29px;background:var(--paper-dark);font-family:"Ubuntu",sans-serif;font-weight:700;font-size:13px;color:var(--brown-dark);border-bottom:1px solid var(--card-border)}
.card-photo{margin:10px auto 0;width:162px;height:96px;background:var(--white);border:1px solid #d9c9ad;display:flex;align-items:center;justify-content:center}
.card-photo div{width:130px;height:70px;border-radius:40% 50% 20% 20%}
.card p{margin-top:6px;font-size:9.5px;line-height:13px;color:var(--ink)}
.card .btn{margin-top:6px;font-weight:400;font-size:10px;padding:3px 7px;border-radius:2px}

/* product detail */
.tabs{position:absolute;left:34px;top:715px;display:flex;gap:5px}
.tab{height:30px;line-height:30px;padding:0 15px;background:var(--paper-dark);border:1px solid var(--card-border);border-bottom:none;border-radius:3px 3px 0 0;font-size:11px;color:var(--ink)}
.tab.on{background:var(--panel);color:var(--brown)}
.detail{position:absolute;left:34px;top:744px;width:830px;height:265px;background:var(--panel);border:1px solid var(--card-border);border-radius:0 3px 3px 3px}
.detail h2{position:absolute;left:24px;top:22px;font-family:"Ubuntu",sans-serif;font-weight:500;font-size:14px;color:var(--ink)}
.features{position:absolute;left:24px;top:53px;list-style:none;font-size:9.5px;color:var(--ink)}
.features li{height:19px}
.features li::before{content:"›";margin-right:5px}
.row{position:absolute;left:24px;font-size:8.5px;font-weight:700;display:flex;align-items:center;gap:5px}
.select{font-weight:400;border:1px solid #c9b798;background:var(--white);padding:3px 6px;font-size:8.5px;display:flex;gap:12px}
.stars{display:flex;gap:2px}
.price{position:absolute;left:24px;top:220px;font-family:"Ubuntu",sans-serif;font-size:14px;font-weight:500;display:flex;align-items:center;gap:16px}
.price .btn{font-family:"Open Sans",sans-serif;font-size:9px;padding:4px 8px;border-radius:2px}
.detail-photo{position:absolute;left:500px;top:24px;width:305px;height:216px;background:var(--white);border:1px solid #d9c9ad;display:flex;align-items:center;justify-content:center}
.detail-photo div{width:280px;height:160px;border-radius:45% 50% 20% 20%;background:linear-gradient(160deg,#2e6f84,#1f5566 65%,#e8e3d6 82%)}
.detail-dots{position:absolute;left:397px;top:252px;display:flex;gap:4px}
.detail-dots i{width:5px;height:5px;border-radius:50%;background:#c9b596}
.detail-dots i.on{background:#8b6c4a}

/* footer */
.footer{position:absolute;left:0;top:1026px;width:896px;height:174px;background:linear-gradient(var(--footer),var(--footer-dark));color:var(--white)}
.follow{position:absolute;left:46px;top:28px;font-family:"Ubuntu",sans-serif;font-size:13px;font-weight:500;display:flex;align-items:center;gap:8px}
.social{width:36px;height:36px;border-radius:50%;background:#6f5a3e}
.footer-brand{position:absolute;left:48px;top:98px;display:flex;align-items:center;gap:10px;font-family:"Ubuntu",sans-serif;font-weight:700;font-size:22px;color:#c9bfb0}
.footer-brand i{width:58px;height:40px;background:#a59c8e;border-radius:4px}
.col{position:absolute;top:22px;font-size:9px;line-height:15px}
.col h4{font-size:10.5px;font-weight:700;margin-bottom:8px}
.col.links li{list-style:none}
.col.links li::before{content:"›";margin-right:5px}
.divider{position:absolute;top:22px;width:1px;height:118px;background:#6f5a3e}
.copyright{position:absolute;left:0;right:0;top:140px;text-align:center;font-size:8.5px;color:#efe4d2;border-top:1px solid #9a8260;padding-top:10px}
</style>
</head>
<body>
<div class="page">

  <header class="header">
    <div class="account"><a href="#">Login</a><span>/</span><a href="#">Register</a></div>
    <div class="cart">
      <div><b>0</b> items - Total: <b>$0.00</b></div>
      <div class="cart-buttons"><a href="#">View Cart</a><a class="dark" href="#">Checkout</a></div>
    </div>
    <div class="nav-band"></div>
    <nav class="nav left"><a class="active" href="#">Home</a><a href="#">About Us</a><a href="#">Products</a></nav>
    <nav class="nav right"><a href="#">Information</a><a href="#">Blog</a><a href="#">Contact Us</a></nav>
    <div class="brand-block">
      <div class="brand-mark"></div>
      <div class="brand">Tovlark</div>
    </div>
  </header>

  <section class="hero">
    <h1 class="hero-title">Lorem ipsum dolor sit amet,</h1>
    <p class="hero-text">Lorem ipsum dolor sit amet, consectetur adipiscing elit. Quisque dictum accumsan quam, in gravida sapien auctor et. Maecenas molestie vestibulum varius. Phasellus id urna</p>
    <a class="btn hero-btn" href="#">More info</a>
    <div class="hero-kid" role="img" aria-label="Photo of a toddler sitting and putting on a shoe"></div>
    <div class="hero-shoe" role="img" aria-label="Photo of a teal leather baby shoe with velcro strap"></div>
    <svg class="arrow prev" width="16" height="80" viewBox="0 0 16 80"><polyline points="14,2 2,40 14,78" fill="none" stroke="#b9a27e" stroke-width="2"/></svg>
    <svg class="arrow next" width="16" height="80" viewBox="0 0 16 80"><polyline points="2,2 14,40 2,78" fill="none" stroke="#b9a27e" stroke-width="2"/></svg>
    <div class="dots"><i class="on"></i><i></i><i></i><i></i><i></i></div>
  </section>

  <section class="cards">
    <article class="card" style="left:34px">
      <h3>TOVIS PEBBLE</h3>
      <div class="card-photo"><div role="img" aria-label="Navy shoe with orange accents" style="background:linear-gradient(150deg,#e07a2e,#2c3f6e 45%,#eeeeee 85%)"></div></div>
      <p>Lorem ipsum dolor sit amet,<br>consectetur adipiscing elit. Quisque</p>
      <a class="btn" href="#">More Info</a>
    </article>
    <article class="card" style="left:248px">
      <h3>TOVIS LUMBO</h3>
      <div class="card-photo"><div role="img" aria-label="Navy and light blue lace-up shoe" style="background:linear-gradient(150deg,#7fb3dc,#2c3f6e 45%,#eeeeee 85%)"></div></div>
      <p>Lorem ipsum dolor sit amet,<br>consectetur adipiscing elit. Quisque</p>
      <a class="btn" href="#">More Info</a>
    </article>
    <article class="card" style="left:462px">
      <h3>TOVIS RUSK</h3>
      <div class="card-photo"><div role="img" aria-label="Teal shoe with velcro strap" style="background:linear-gradient(150deg,#2e6f84,#1f5566 55%,#eeeeee 85%)"></div></div>
      <p>Lorem ipsum dolor sit amet,<br>consectetur adipiscing elit. Quisque</p>
      <a class="btn" href="#">More Info</a>
    </article>
    <article class="card" style="left:676px">
      <h3>TOVIS SMALLE</h3>
      <div class="card-photo"><div role="img" aria-label="White leather shoe with strap" style="background:linear-gradient(150deg,#f4f2ec,#dcd8cc 60%,#f2f0ea 85%)"></div></div>
      <p>Lorem ipsum dolor sit amet,<br>consectetur adipiscing elit. Quisque</p>
      <a class="btn" href="#">More Info</a>
    </article>
  </section>

  <div class="tabs">
    <div class="tab on">Pebble</div><div class="tab">Lumbo</div><div class="tab">Tumble</div><div class="tab">Stride</div>
  </div>
  <section class="detail">
    <h2>Tovis Pebble</h2>
    <ul class="features">
      <li>Outside of soft leather</li>
      <li>Inside and inner sole of leather</li>
      <li>Outsole naturummi, extended on the back</li>
      <li>Ortho custom insole</li>
      <li>Zips all the way from the side and under the foot makes the shoe easy to put on and take off</li>
      <li>Torsional read for better support of ankle</li>
    </ul>
    <div class="row" style="top:168px">Choose Shoes Size:
      <span class="select">15/16 (8,5-9,5cm)
        <svg width="8" height="8" viewBox="0 0 8 8"><polygon points="1,2 7,2 4,6" fill="#4a3a2a"/></svg>
      </span>
    </div>
    <div class="row" style="top:196px">Customer Rating:
      <span class="stars">
        <svg width="14" height="14" viewBox="0 0 24 24"><polygon points="12,2 15,9 22,9 16.5,14 18.5,21 12,17 5.5,21 7.5,14 2,9 9,9" fill="#f0a020"/></svg>
        <svg width="14" height="14" viewBox="0 0 24 24"><polygon points="12,2 15,9 22,9 16.5,14 18.5,21 12,17 5.5,21 7.5,14 2,9 9,9" fill="#f0a020"/></svg>
        <svg width="14" height="14" viewBox="0 0 24 24"><polygon points="12,2 15,9 22,9 16.5,14 18.5,21 12,17 5.5,21 7.5,14 2,9 9,9" fill="#f0a020"/></svg>
        <svg width="14" height="14" viewBox="0 0 24 24"><polygon points="12,2 15,9 22,9 16.5,14 18.5,21 12,17 5.5,21 7.5,14 2,9 9,9" fill="#f0a020"/></svg>
        <svg width="14" height="14" viewBox="0 0 24 24"><polygon points="12,2 15,9 22,9 16.5,14 18.5,21 12,17 5.5,21 7.5,14 2,9 9,9" fill="#7d7d7d"/></svg>
      </span>
    </div>
    <div class="price">Price:&nbsp;399kr <a class="btn" href="#">Add to Cart</a></div>
    <div class="detail-photo"><div role="img" aria-label="Large photo of the teal leather baby shoe"></div></div>
    <div class="detail-dots"><i class="on"></i><i></i><i></i><i></i></div>
  </section>

  <footer class="footer">
    <div class="follow">Follow Us:
      <span class="social" aria-label="Social link"></span><span class="social" aria-label="Social link"></span><span class="social" aria-label="Social link"></span><span class="social" aria-label="Social link"></span>
    </div>
    <div class="footer-brand"><i></i>Tovlark</div>
    <div class="divider" style="left:336px"></div>
    <div class="col links" style="left:385px">
      <h4>Tovlark</h4>
      <ul><li>About Us</li><li>Press</li><li>In the media</li><li>Work for us</li><li>Become a Reseller</li></ul>
    </div>
    <div class="divider" style="left:516px"></div>
    <div class="col links" style="left:559px">
      <h4>Information</h4>
      <ul><li>Frequently asked questions</li><li>Contact Us</li><li>Terms</li><li>Cookies and privacy</li></ul>
    </div>
    <div class="divider" style="left:729px"></div>
    <div class="col" style="left:772px">
      <h4>Address</h4>
      <div>Tovlark / Marvenn</div><div>Box 18 302</div><div>Norrvik 41518</div><div>Tel 031-480 26 15</div>
    </div>
    <div class="copyright">Copyrights © 2012-2013 Tovlark. All Rights Reserved</div>
  </footer>

</div>
</body>
</html>
```